Brantley Advisory Group provides support for renewable energy projects to utilities and suppliers

I need a professional looking business card that is both simple and elegant and unique. My clients are mostly large organizations not individuals. I am a consultant with my own company that is small but would like to give clients the impression I am larger. Smart grid, fiber optics, software, field hardware, distribution automation, substation automation, operations, energy storage/batteries, microgrids, customer service, strategy/roadmaps, conservation, Automated Metering Infrastruture (AMI or smart meters) are all areas of focus.

Target Market(s)

Utilities, suppliers, governmental agencies involved in energy. All types of energy especially natural gas and electrical. Especially renewable energy or green projects.

Contact Information for Business Card

Name - Ross Brantley Cell Phone - 425.318.4762 Email - rbrantley@brantleyag-example.com
Company - Brantley Advisory Group (logo) Title - Principal

Font styles to use
Serif
Sans Serif

Colors

Designer to choose colors to be used in the design.

Requirements
Must have
• Simple and professional and powerful.
• Unique/creative design.
Nice to have
• Utilize color scheme to accent logo colors. Maybe some geometric pattern on edge of card with color.
Should not have
• Busy, complicated, traditional

```html
<!DOCTYPE html>
<html lang="en">
<head>
<meta charset="utf-8">
<title>Brantley Advisory Group – Business Card</title>
<link rel="stylesheet" href="https://fonts.googleapis.com/css2?family=Montserrat:wght@400;700&display=swap">
<style>
  :root {
    --backdrop: #e9e6e2;
    --card: #ffffff;
    --brand-blue: #2424a0;
    --brand-green: #6a9a45;
    --ink: #3a3a3a;
    --shadow: rgba(40, 30, 20, 0.22);
  }
  * { margin: 0; padding: 0; box-sizing: border-box; }
  html, body {
    width: 1200px; height: 909px; overflow: hidden;
    background: var(--backdrop);
    font-family: "Montserrat", Arial, sans-serif;
  }
  .stage { position: relative; width: 1200px; height: 909px; }
  .card {
    position: absolute;
    width: 560px; height: 320px;
    background: var(--card);
    box-shadow: 0 6px 18px var(--shadow);
  }
  .card--front { left: 60px; top: 90px; }
  .card--back { left: 580px; top: 500px; }

  .brand { display: flex; align-items: center; gap: 14px; }
  .brand__mark { width: 22px; height: 22px; background: var(--brand-green); flex: none; }
  .brand__name {
    font-weight: 700; color: var(--brand-blue);
    letter-spacing: 0.01em; white-space: nowrap;
  }

  .card--front .brand {
    position: absolute; left: 50%; top: 50%;
    transform: translate(-50%, -50%);
  }
  .card--front .brand__mark { width: 30px; height: 30px; }
  .card--front .brand__name { font-size: 30px; }

  .card--back .brand { position: absolute; left: 40px; top: 44px; gap: 10px; }
  .card--back .brand__name { font-size: 18px; }
  .card--back .brand__mark { width: 16px; height: 16px; }

  .person { position: absolute; right: 36px; top: 44px; text-align: right; }
  .person__name { font-weight: 700; font-size: 21px; color: var(--brand-blue); }
  .person__title { font-size: 13px; color: var(--ink); margin-top: 2px; }

  .divider {
    position: absolute; left: 150px; right: 30px; top: 112px;
    height: 1px; background: var(--brand-green);
  }

  .contact {
    position: absolute; right: 36px; top: 130px;
    text-align: right; font-size: 13px; line-height: 1.9; color: var(--ink);
  }
</style>
</head>
<body>
  <main class="stage">
    <section class="card card--front" aria-label="Card front">
      <div class="brand">
        <span class="brand__mark"></span>
        <span class="brand__name">Brantley Advisory Group</span>
      </div>
    </section>

    <section class="card card--back" aria-label="Card back">
      <div class="brand">
        <span class="brand__mark"></span>
        <span class="brand__name">Brantley Advisory Group</span>
      </div>
      <div class="person">
        <p class="person__name">Ross Brantley</p>
        <p class="person__title">Principal</p>
      </div>
      <div class="divider"></div>
      <div class="contact">
        <p class="contact__phone">425.318.4762</p>
        <p class="contact__email">rbrantley@brantleyag-example.com</p>
      </div>
    </section>
  </main>
</body>
</html>
```